Rw building ventures pty ltd

This is a development and construction company. Website can be set up on our domain rwbuildworks.net if we could change the domain to rwbuildworks.com.au would be great

Want the page to have eye catching designs, red, black and white are the preffered colours.

Check out www.toluqin.com.au it is my former company with my partner which i am now venturing out on my own, that is the perfect example of the website i want even allot of the information would be the same

Industry/Entity Type

Construction

Coding

Coded - Design and coding required

Number of Pages Required

5+ page

Requirements
Must have
• Company logo eye catching designs

```html
<!DOCTYPE html>
<html lang="en">
<head>
<meta charset="utf-8">
<title>RW Buildworks</title>
<link href="https://fonts.googleapis.com/css2?family=Montserrat:wght@300;400;500;600;700;800&display=swap" rel="stylesheet">
<style>
:root{
  --red:#e30613;
  --black:#0e0f11;
  --dark:#17181b;
  --white:#ffffff;
  --ink:#222;
  --grey:#555;
  --line:#9a9a9a;
}
*{margin:0;padding:0;box-sizing:border-box}
html,body{width:1200px;height:5115px;overflow:hidden}
body{position:relative;background:var(--white);font-family:"Montserrat",sans-serif;color:var(--ink)}
.abs{position:absolute}
.center{left:0;width:1200px;text-align:center}

/* header */
.site-header{top:0;left:0;width:1200px;height:103px;background:var(--white)}
.brand{left:110px;top:24px;font-size:24px;font-weight:700;color:var(--ink);letter-spacing:1px;display:flex;align-items:center;gap:10px}
.brand-mark{width:26px;height:26px;background:var(--red)}
.main-nav a{position:absolute;top:42px;font-size:15px;font-weight:500;color:var(--ink);text-decoration:none}
.btn-solid{background:var(--red);color:var(--white);font-size:15px;display:flex;align-items:center;justify-content:center;font-weight:500}
.btn-outline{border:2px solid var(--red);color:var(--red);font-size:15px;display:flex;align-items:center;justify-content:center;font-weight:500;border-radius:3px}

/* hero */
.hero{top:103px;left:0;width:1200px;height:742px;background:linear-gradient(180deg,#8fb6dc 0%,#c9d9e6 35%,#dcdad2 60%,#6f7a58 85%,#8b8b86 100%)}
.hero-box{left:213px;top:378px;width:806px;height:199px;background:rgba(20,20,22,.78)}
.hero-title{top:400px;font-size:58px;font-weight:700;color:var(--red)}
.hero-text{top:468px;font-size:16px;line-height:26px;color:var(--white)}
.dot{width:16px;height:16px;border-radius:50%;background:var(--white);top:616px}

/* welcome */
.welcome-kicker{left:111px;top:912px;font-size:44px;font-weight:300}
.welcome-title{left:111px;top:966px;font-size:42px;font-weight:700;color:var(--red)}
.welcome-text{left:111px;top:1033px;width:475px;font-size:13px;line-height:26.6px;color:var(--ink)}
.collage{left:604px;top:914px;width:493px;height:366px;border:5px solid var(--red);background:var(--red)}
.collage div{position:absolute}

/* dark sections */
.dark{left:0;width:1200px;background:linear-gradient(180deg,#222327,#121316 60%,#1b1c1f)}
.section-kicker{font-size:44px;font-weight:300;color:var(--white)}
.section-kicker.on-light{color:var(--ink)}
.section-title{font-size:42px;font-weight:700;color:var(--red)}
.section-text{font-size:14px;line-height:26px;color:#e6e6e6}
.service-card{top:1645px;width:318px;height:344px}
.service-card .photo{height:286px}
.service-label{height:58px;background:var(--white);display:flex;align-items:center;justify-content:space-between;padding:0 24px;font-size:17px;color:var(--ink)}
.service-label.active{background:var(--red);color:var(--white)}
.service-label svg{width:20px;height:20px}

/* testimonial */
.quote-card{left:229px;top:2418px;width:741px;height:268px;background:var(--white);border-radius:22px;box-shadow:0 4px 16px rgba(0,0,0,.16)}
.quote-text{left:310px;top:2494px;width:580px;text-align:center;font-size:13.5px;line-height:24.5px;color:var(--grey)}
.nav-arrow{width:34px;height:34px;border-radius:50%;top:2560px;display:flex;align-items:center;justify-content:center}

/* projects */
.project{background:#888}

/* contact */
.contact{top:4004px;left:0;width:1200px;height:715px;background:linear-gradient(135deg,#f2efec,#fbfaf8 45%,#ebe8e6)}
.contact-title{top:4092px;font-size:44px;font-weight:400;line-height:54px;color:var(--ink)}
.field{left:356px;width:489px;border:1px solid #555;background:var(--white);font-size:14px;color:#333;padding:12px 14px}

/* footer */
.site-footer{top:4719px;left:0;width:1200px;height:396px;background:var(--black)}
.footer-brand{top:4776px;font-size:56px;font-weight:700;color:var(--white);letter-spacing:3px}
.footer-contact{top:4912px;font-size:14px;color:var(--red)}
.footer-nav{top:5012px;font-size:14px;color:var(--white);word-spacing:2px}
.copyright{top:5049px;font-size:13px;color:var(--white)}
.social{width:30px;height:30px;border:2px solid var(--white);border-radius:50%;top:4956px}
</style>
</head>
<body>

<header class="abs site-header">
  <div class="abs brand"><span class="brand-mark"></span>RW BUILDWORKS</div>
  <nav class="main-nav">
    <a style="left:405px">HOME</a>
    <a style="left:477px">ABOUT US</a>
    <a style="left:580px">SERVICES</a>
    <a style="left:678px">PROJECTS</a>
    <a style="left:781px">CONTACT US</a>
  </nav>
  <a class="abs btn-solid" style="left:910px;top:34px;width:179px;height:36px">WORK WITH US</a>
</header>

<section class="abs hero" role="img" aria-label="Modern white apartment buildings lining a paved courtyard under a blue sky">
  <div class="abs hero-box"></div>
  <h1 class="abs center hero-title">Neque porro quisquam</h1>
  <p class="abs center hero-text">Book a virtual appointment and see a doctor that same day. Skip the waiting<br>room and skip waiting for a call back from your physician</p>
  <a class="abs btn-solid" style="left:479px;top:537px;width:242px;height:40px">Book a Your Appointment</a>
  <span class="abs dot" style="left:570px;background:var(--red)"></span>
  <span class="abs dot" style="left:596px"></span>
  <span class="abs dot" style="left:620px"></span>
  <span class="abs dot" style="left:644px"></span>
  <svg class="abs" style="left:0;top:0" width="1200" height="742" viewBox="0 0 1200 742">
    <path d="M0 582 Q600 862 1200 582 V742 H0 Z" fill="#fff"/>
    <path d="M0 598 Q600 888 1200 598" fill="none" stroke="#e30613" stroke-width="6"/>
  </svg>
</section>

<section>
  <h2 class="abs welcome-kicker">Welcome to</h2>
  <h2 class="abs welcome-title">RW Buildworks</h2>
  <p class="abs welcome-text">Sed ut perspiciatis unde omnis iste natus error sit voluptatem accusantium doloremque laudantium, totam rem aperiam, eaque ipsa quae ab illo inventore veritatis et quasi architecto beatae vitae dicta sunt explicabo. Nemo enim ipsam voluptatem quia voluptas sit aspernatur aut odit aut fugit, sed quia consequuntur magni dolores eos qui ratione voluptatem sequi</p>
  <a class="abs btn-outline" style="left:111px;top:1224px;width:161px;height:44px">Learn More</a>
  <div class="abs collage">
    <div role="img" aria-label="Smiling woman in front of colleagues reviewing plans" style="left:3px;top:3px;width:285px;height:350px;background:linear-gradient(135deg,#6b5646,#c9b7a3 55,#8a8f96)"></div>
    <div role="img" aria-label="Building skeletons at sunset on a construction site" style="left:294px;top:3px;width:186px;height:170px;background:linear-gradient(180deg,#d7d5c5,#8b7c55 60%,#3c3527)"></div>
    <div role="img" aria-label="White modern townhouses" style="left:294px;top:181px;width:186px;height:172px;background:linear-gradient(180deg,#a9c2dc,#e6e6e4 50%,#6f7464)"></div>
  </div>
</section>

<section class="abs dark" style="top:1340px;height:856px">
  <svg class="abs" style="left:0;top:0" width="1200" height="170" viewBox="0 0 1200 170">
    <path d="M0 0 H1200 V170 Q600 -130 0 170 Z" fill="#fff"/>
    <path d="M0 150 Q600 -140 1200 150" fill="none" stroke="#e30613" stroke-width="6"/>
  </svg>
  <p class="abs center section-kicker" style="top:108px">RW</p>
  <h2 class="abs center section-title" style="top:160px">What We Do</h2>
  <p class="abs center section-text" style="top:229px">Sed ut perspiciatis unde omnis iste natus error sit voluptatem<br>accusantium doloremque laudantium, totam rem aperiam, eaque ipsa quae ab illo inventore veritatis</p>
</section>

<article class="abs service-card" style="left:107px">
  <div class="photo" role="img" aria-label="Modern white terrace houses" style="background:linear-gradient(180deg,#9fbfe0,#e1e1dc 45%,#8a8f7a)"></div>
  <div class="service-label">Neque porro quisquam<svg viewBox="0 0 20 20"><circle cx="10" cy="10" r="9" fill="#111"/><path d="M6 10h7M10 6.5l3.5 3.5L10 13.5" stroke="#fff" stroke-width="2" fill="none"/></svg></div>
</article>
<article class="abs service-card" style="left:441px">
  <div class="photo" role="img" aria-label="High-rise construction site at dusk" style="background:linear-gradient(180deg,#27323a,#8a7d57 55%,#3a2f22)"></div>
  <div class="service-label active">Neque porro quisquam<svg viewBox="0 0 20 20"><circle cx="10" cy="10" r="9" fill="#fff"/><path d="M6 10h7M10 6.5l3.5 3.5L10 13.5" stroke="#e30613" stroke-width="2" fill="none"/></svg></div>
</article>
<article class="abs service-card" style="left:773px">
  <div class="photo" role="img" aria-label="Red crane beside a glass tower under blue sky" style="background:linear-gradient(135deg,#c99a2e,#2e5fa8 50%,#8fb4e4)"></div>
  <div class="service-label">Neque porro quisquam<svg viewBox="0 0 20 20"><circle cx="10" cy="10" r="9" fill="#111"/><path d="M6 10h7M10 6.5l3.5 3.5L10 13.5" stroke="#fff" stroke-width="2" fill="none"/></svg></div>
</article>
<a class="abs btn-outline" style="left:479px;top:2029px;width:242px;height:40px">WORK WITH US</a>

<section>
  <p class="abs center section-kicker on-light" style="top:2277px">RW</p>
  <h2 class="abs center section-title" style="top:2330px">Our Clients Say</h2>
  <svg class="abs" style="left:840px;top:2680px" width="80" height="50" viewBox="0 0 80 50"><path d="M0 0 H70 L74 46 L40 4 Z" fill="#fff"/></svg>
  <div class="abs quote-card"></div>
  <svg class="abs" style="left:580px;top:2448px" width="40" height="34" viewBox="0 0 40 34"><path d="M4 0h14v16c0 9-5 15-13 18l-2-4c5-2 7-5 7-10H4Z M22 0h14v16c0 9-5 15-13 18l-2-4c5-2 7-5 7-10h-6Z" fill="#e30613"/></svg>
  <p class="abs quote-text">Sed ut perspiciatis unde omnis iste natus error sit voluptatem accntium doloremque laudantium, totam rem aperiam, eaque ipsa quae ab illo intore veritatis et quasi architecto beatae vitae dicta sunt explicabo. Nemo enim ipsam voluptatem quia voluptas sit aspernatur aut odit aut fugit, sed quia consequuntur magni dolores eos qui ratione</p>
  <svg class="abs" style="left:550px;top:2638px" width="100" height="18" viewBox="0 0 100 18">
    <g fill="#e0a100">
      <path id="st" d="M9 0l2.6 5.6 6.1.7-4.5 4.1 1.2 6L9 13.4 3.6 16.4l1.2-6L.3 6.3l6.1-.7Z"/>
      <use href="#st" x="20"/><use href="#st" x="40"/><use href="#st" x="60"/><use href="#st" x="80"/>
    </g>
  </svg>
  <span class="abs nav-arrow" style="left:210px;background:#111"><svg width="14" height="14" viewBox="0 0 14 14"><path d="M9 2L4 7l5 5" stroke="#fff" stroke-width="2" fill="none"/></svg></span>
  <span class="abs nav-arrow" style="left:951px;background:var(--red)"><svg width="14" height="14" viewBox="0 0 14 14"><path d="M5 2l5 5-5 5" stroke="#fff" stroke-width="2" fill="none"/></svg></span>
  <div class="abs" role="img" aria-label="Client portrait" style="left:574px;top:2718px;width:88px;height:88px;border-radius:50%;background:radial-gradient(circle,#d9b49a,#7f6b5d);box-shadow:0 3px 10px rgba(0,0,0,.25)"></div>
</section>

<section class="abs dark" style="top:2920px;height:1084px">
  <svg class="abs" style="left:0;top:0" width="1200" height="170" viewBox="0 0 1200 170">
    <path d="M0 0 H1200 V170 Q600 -130 0 170 Z" fill="#fff"/>
    <path d="M0 150 Q600 -140 1200 150" fill="none" stroke="#e30613" stroke-width="6"/>
  </svg>
  <p class="abs center section-kicker" style="top:104px">RW</p>
  <h2 class="abs center section-title" style="top:157px">Our Latest Projects</h2>
  <p class="abs center section-text" style="top:226px">Sed ut perspiciatis unde omnis iste natus error sit voluptatem<br>accusantium doloremque laudantium, totam rem aperiam, eaque ipsa quae ab illo inventore veritatis</p>
</section>
<div class="abs project" role="img" aria-label="Brick and render townhouses" style="left:107px;top:3223px;width:318px;height:286px;background:linear-gradient(180deg,#e9ecef,#a77a56 50%,#5c5148)"></div>
<div class="abs project" role="img" aria-label="Cranes over a building site under a purple evening sky" style="left:441px;top:3223px;width:650px;height:286px;background:linear-gradient(180deg,#4a4a9a,#b067b8 45%,#e09a6a 70%,#231a1c)"></div>
<div class="abs project" role="img" aria-label="White apartment block with balconies and trees" style="left:107px;top:3527px;width:650px;height:284px;background:linear-gradient(180deg,#dfe4ea,#b8bcb8 55%,#5f6e49)"></div>
<div class="abs project" role="img" aria-label="White modern house with garage" style="left:773px;top:3527px;width:318px;height:284px;background:linear-gradient(180deg,#c5ccd5,#f1f1ef 50%,#8e8f8c)"></div>
<a class="abs btn-outline" style="left:479px;top:3851px;width:242px;height:42px">SEE MORE</a>

<section class="abs contact" role="img" aria-label="Faded photo of a person working at a laptop"></section>
<h2 class="abs center contact-title">Let’s build your dream<br>home together! <strong style="color:var(--red);font-weight:700">Say Hello!</strong></h2>
<div class="abs field" style="top:4232px;height:50px">Your Name</div>
<div class="abs field" style="top:4292px;height:50px">Email</div>
<div class="abs field" style="top:4352px;height:51px">Phone</div>
<div class="abs field" style="top:4411px;height:137px">Message</div>
<a class="abs btn-solid" style="left:356px;top:4562px;width:161px;height:44px">Submite Now</a>

<footer class="abs site-footer"></footer>
<p class="abs center footer-brand">RW BUILDWORKS<span style="color:var(--white)">.</span></p>
<p class="abs center footer-contact">
  <svg width="16" height="16" viewBox="0 0 16 16" style="vertical-align:-3px"><path d="M3 1l3 3-2 2c1 2 3 4 5 5l2-2 3 3-2 3C7 15 1 9 1 3Z" fill="none" stroke="#e30613" stroke-width="1.4"/></svg>
  &nbsp;Phone: 0123 456 780 &nbsp;&nbsp;&nbsp;&nbsp;&nbsp;&nbsp;&nbsp;
  <svg width="18" height="14" viewBox="0 0 18 14" style="vertical-align:-2px"><rect x="1" y="1" width="16" height="12" fill="none" stroke="#e30613" stroke-width="1.4"/><path d="M1 1l8 7 8-7" fill="none" stroke="#e30613" stroke-width="1.4"/></svg>
  &nbsp;Email: info@rwbuildworks.com.au
</p>
<span class="abs social" style="left:550px"></span>
<span class="abs social" style="left:585px"></span>
<span class="abs social" style="left:620px"></span>
<p class="abs center footer-nav">HOME &nbsp;&nbsp;| &nbsp;&nbsp;ABOUT US &nbsp;&nbsp;| &nbsp;&nbsp;SERVICES &nbsp;&nbsp;| &nbsp;&nbsp;PROJECTS &nbsp;&nbsp;| &nbsp;&nbsp;CONTACT US</p>
<p class="abs center copyright">RW Buildworks (c) 2021 &nbsp;| All Rights Reserved</p>

</body>
</html>
```